Dunwick Consulting Powerpoint Template

I require a powerpoint template that I can use for presentations and for report writing. Template should include:
* Cover page with company logo and space for presentation title, and client logo if required.
* Proposed font and heading styles to match the logo (demonstrated through some sample text)
* Three different examples of presentation pages that can be tailored to different clients
* End page for contact details of the presenter or other report details. (so template should be five pages in total length)

The overall style of the template is professional, but with an eye-catching style.

Target Market(s)

Government clients

Industry/Entity Type

Government

Requirements
Must have
• Three different presentation pages that can be optional.
• Proposed font / heading styles for presentation with sample texts
• Use colour pallet: http://www.huetrellis.net/palette/417096/Velvet_Harbor
• Clear, crisp and professional design.
Should not have
• Pictures

```html
<!DOCTYPE html>
<html lang="en">
<head>
<meta charset="utf-8">
<title>Dunwick Consulting – Cover</title>
<link rel="stylesheet" href="https://fonts.googleapis.com/css2?family=Jost:wght@300;400&family=Lato:wght@400&display=swap">
<style>
  :root {
    --hero-deep: #7f9598;
    --hero-mid: #93a7aa;
    --hero-light: #aebdbf;
    --paper: #ffffff;
    --ink-navy: #1f3148;
    --mark-fill: #a3b5b4;
    --footer-band: #9fb1b0;
    --footer-text: #ffffff;
    --title-text: #ffffff;
  }
  * { box-sizing: border-box; margin: 0; padding: 0; }
  html, body {
    width: 1200px;
    height: 688px;
    overflow: hidden;
    background: var(--paper);
  }
  .slide {
    position: relative;
    width: 1200px;
    height: 688px;
    background: var(--paper);
    font-family: "Jost", "Futura", sans-serif;
  }
  .hero {
    position: absolute;
    left: 0; top: 0;
    width: 1200px;
    height: 423px;
    background:
      radial-gradient(ellipse at 70% 35%, var(--hero-light) 0%, transparent 55%),
      linear-gradient(100deg, var(--hero-light) 0%, var(--hero-mid) 45%, var(--hero-deep) 100%);
  }
  .hero-title {
    position: absolute;
    left: 0; right: 0;
    top: 214px;
    text-align: center;
    color: var(--title-text);
    font-weight: 300;
    font-size: 50px;
    letter-spacing: 1px;
    line-height: 1;
  }
  .brand {
    position: absolute;
    left: 0; right: 0;
    top: 450px;
    display: flex;
    flex-direction: column;
    align-items: center;
  }
  .brand-dot {
    width: 94px;
    height: 94px;
  }
  .brand-name {
    margin-top: 14px;
    color: var(--ink-navy);
    font-weight: 300;
    text-align: center;
    text-transform: uppercase;
    line-height: 1;
  }
  .brand-name .primary {
    display: block;
    font-size: 46px;
    letter-spacing: 18px;
    padding-left: 18px;
  }
  .brand-name .secondary {
    display: block;
    margin-top: 6px;
    font-size: 17px;
    letter-spacing: 8px;
    padding-left: 8px;
  }
  .footer {
    position: absolute;
    left: 0; bottom: 0;
    width: 1200px;
    height: 34px;
    background: var(--footer-band);
    color: var(--footer-text);
    font-family: "Lato", "Calibri", sans-serif;
    font-size: 14px;
    display: flex;
    justify-content: space-between;
    align-items: center;
    padding: 0 14px;
  }
</style>
</head>
<body>
  <main class="slide">
    <section class="hero" role="img" aria-label="Photo of a business team in a meeting around a table, tinted blue-grey">
      <h1 class="hero-title">PERSENTATION TITLE HERE</h1>
    </section>

    <div class="brand">
      <svg class="brand-dot" viewBox="0 0 94 94" aria-hidden="true">
        <circle cx="47" cy="47" r="45" fill="var(--mark-fill)"/>
      </svg>
      <p class="brand-name">
        <span class="primary">Dunwick</span>
        <span class="secondary">Consulting</span>
      </p>
    </div>

    <footer class="footer">
      <span class="footer-copyright">Copyright there here</span>
      <span class="footer-page">Page : 01</span>
    </footer>
  </main>
</body>
</html>
```